Need posters that inspire entrepreneurs

I want to create beautiful, inspiring wall art. I'm looking for a designer to create an awesome sample (note this sample is not for real use). The winning design will form the foundation of our art "style" so there will be LOTS of ongoing work for the winning designer.

It's your challenge to create a style that is clean, inspiring and timeless, and possibly can be adapted to different colour palettes.

Looking for a perfect execution of words, image and design.

The attached example shows one idea. It should serve as an idea only.

Format of the images should be either rectangular or square. Exact size is preferably UK A4 (US letter) or max A3. Assume that a display would consist of a 4 x 4 image grid so size needs to allow for that in a small to medium size office.

The quotes I want in the 3 samples (each in an individual poster - not combined in 1 poster). Each quote should have it's own, the reason for three is to prove the design work on more than one quote. The quotes are:

1) Failure is the condiment that gives success its flavor.
– Wendell Ruskin

2) Whether you think you can or think you can’t, you’re right.
– Milo Dagwell

3) Ever tried. Ever failed. No matter. Try Again. Fail again. Fail better.
– Oswin Tarrant

Each design should include the image of the person and the quote + any design elements you consider relevant. You should find relevant images of the individuals being quoted. The final images will not be published or used commercially in any way.

Font styles to use
Serif
Sans Serif

Colors

Designer to choose colors to be used in the design.

Requirements
Must have
• Words and headshot image - 1 per poster design.
• Please consider in the design that there will not always be photographs of the person quoted and as such the design will need to hold, whether the source is a photo, sketch or something else.
Nice to have
• None, but note that the final image will be printed on a wall mounted board, printed to the edge but not on the edge. The board will have black or white edges so consider in the design.
Should not have
• None

```html
<!DOCTYPE html>
<html lang="en">
<head>
<meta charset="utf-8">
<title>Quote Posters</title>
<link rel="stylesheet" href="https://fonts.googleapis.com/css2?family=Fira+Sans+Extra+Condensed:wght@500&display=swap">
<style>
  :root {
    --canvas-bg: #000000;
    --frame: #3b3b3b;
    --frame-line: #ffffff;
    --paper: #ffffff;
    --ink: #555555;
    --pill: #555555;
    --pill-text: #ffffff;
    --wedge: #5a5a5a;
    --wedge-stripe: #f2f2f2;
    --blue-light: #1f8fe0;
    --blue-deep: #1c3f9c;
    --photo-light: #e6e6e6;
    --photo-mid: #9a9a9a;
    --photo-dark: #2e2e2e;
  }
  html, body {
    margin: 0;
    padding: 0;
    width: 734px;
    height: 1200px;
    overflow: hidden;
    background: var(--canvas-bg);
  }
  .poster-wall {
    position: relative;
    width: 734px;
    height: 1200px;
  }
  .poster {
    position: absolute;
    left: 114px;
    width: 507px;
    height: 356px;
    display: block;
  }
  .poster--first { top: 52px; }
  .poster--second { top: 422px; }
  .poster--third { top: 792px; }
  .quote-text {
    font-family: "Fira Sans Extra Condensed", "Arial Narrow", sans-serif;
    font-weight: 500;
    font-size: 32px;
    letter-spacing: -0.3px;
    fill: var(--ink);
  }
  .author-name {
    font-family: "Fira Sans Extra Condensed", "Arial Narrow", sans-serif;
    font-weight: 500;
    font-size: 18px;
    fill: var(--pill-text);
  }
  .frame-outer { fill: var(--frame); }
  .frame-line { fill: none; stroke: var(--frame-line); stroke-width: 3; }
  .paper { fill: var(--paper); }
  .author-pill { fill: var(--pill); }
  .corner-wedge { fill: var(--wedge); }
  .wedge-stripe { stroke: var(--wedge-stripe); stroke-width: 2.5; fill: none; }
  .paper-hatch { stroke: #ececec; stroke-width: 1; }
</style>
</head>
<body>
<main class="poster-wall">

  <svg width="0" height="0" style="position:absolute">
    <defs>
      <linearGradient id="portraitBase" x1="0" y1="0" x2="1" y2="0">
        <stop offset="0" stop-color="var(--photo-light)" stop-opacity="0"/>
        <stop offset="0.3" stop-color="var(--photo-light)" stop-opacity="0.9"/>
        <stop offset="0.65" stop-color="var(--photo-mid)"/>
        <stop offset="1" stop-color="var(--photo-dark)"/>
      </linearGradient>
      <radialGradient id="portraitGlow" cx="0.5" cy="0.5" r="0.5">
        <stop offset="0" stop-color="#d8d8d8"/>
        <stop offset="0.6" stop-color="#b8b8b8" stop-opacity="0.7"/>
        <stop offset="1" stop-color="#b8b8b8" stop-opacity="0"/>
      </radialGradient>
      <radialGradient id="portraitShade" cx="0.5" cy="0.5" r="0.5">
        <stop offset="0" stop-color="var(--photo-dark)"/>
        <stop offset="0.7" stop-color="var(--photo-dark)" stop-opacity="0.6"/>
        <stop offset="1" stop-color="var(--photo-dark)" stop-opacity="0"/>
      </radialGradient>
      <linearGradient id="blueBand" x1="0" y1="1" x2="1" y2="0">
        <stop offset="0" stop-color="var(--blue-light)"/>
        <stop offset="1" stop-color="var(--blue-deep)"/>
      </linearGradient>
    </defs>
  </svg>

  <svg class="poster poster--first" viewBox="0 0 633 445" xmlns="http://www.w3.org/2000/svg">
    <rect class="frame-outer" width="633" height="445"/>
    <rect class="paper" x="9" y="8" width="615" height="429"/>
    <g class="paper-hatch">
      <line x1="9" y1="40" x2="80" y2="8"/><line x1="9" y1="55" x2="110" y2="8"/><line x1="9" y1="70" x2="140" y2="8"/>
    </g>
    <g class="portrait-slot" role="img" aria-label="Black and white portrait photograph of Wendell Ruskin">
      <rect x="230" y="8" width="394" height="429" fill="url(#portraitBase)"/>
      <rect x="370" y="20" width="200" height="280" fill="url(#portraitGlow)"/>
      <rect x="340" y="250" width="300" height="200" fill="url(#portraitShade)"/>
    </g>
    <polygon class="corner-wedge" points="9,280 335,437 9,437"/>
    <line class="wedge-stripe" x1="9" y1="289" x2="316" y2="437"/>
    <line class="wedge-stripe" x1="9" y1="296" x2="302" y2="437"/>
    <line class="wedge-stripe" x1="9" y1="303" x2="288" y2="437"/>
    <polygon points="296,437 624,437 624,298" fill="url(#blueBand)"/>
    <text class="quote-text" x="55" y="93">Failure is the condiment</text>
    <text class="quote-text" x="55" y="136">that gives success</text>
    <text class="quote-text" x="55" y="179">its flavor.</text>
    <path class="author-pill" d="M193,243 H310 C316,237 314,229 308,222 C328,227 341,241 339,259 A15,15 0 0 1 324,275 H193 A16,16 0 0 1 193,243 Z"/>
    <text class="author-name" x="259" y="265" text-anchor="middle">Wendell Ruskin</text>
    <rect class="frame-line" x="7.5" y="6.5" width="618" height="432"/>
  </svg>

  <svg class="poster poster--second" viewBox="0 0 633 445" xmlns="http://www.w3.org/2000/svg">
    <rect class="frame-outer" width="633" height="445"/>
    <rect class="paper" x="9" y="8" width="615" height="429"/>
    <g class="paper-hatch">
      <line x1="9" y1="40" x2="80" y2="8"/><line x1="9" y1="55" x2="110" y2="8"/><line x1="9" y1="70" x2="140" y2="8"/>
    </g>
    <g class="portrait-slot" role="img" aria-label="Black and white portrait photograph of Milo Dagwell">
      <rect x="230" y="8" width="394" height="429" fill="url(#portraitBase)"/>
      <rect x="320" y="15" width="220" height="300" fill="url(#portraitGlow)"/>
      <rect x="330" y="280" width="300" height="180" fill="url(#portraitShade)"/>
    </g>
    <polygon class="corner-wedge" points="9,280 335,437 9,437"/>
    <line class="wedge-stripe" x1="9" y1="289" x2="316" y2="437"/>
    <line class="wedge-stripe" x1="9" y1="296" x2="302" y2="437"/>
    <line class="wedge-stripe" x1="9" y1="303" x2="288" y2="437"/>
    <polygon points="296,437 624,437 624,298" fill="url(#blueBand)"/>
    <text class="quote-text" x="64" y="90">Whether you think</text>
    <text class="quote-text" x="64" y="133">you can or think</text>
    <text class="quote-text" x="64" y="176">you can’t, you’re right.</text>
    <path class="author-pill" d="M152,242 H270 C276,236 274,228 268,221 C288,226 301,240 299,258 A15,15 0 0 1 284,274 H152 A16,16 0 0 1 152,242 Z"/>
    <text class="author-name" x="216" y="264" text-anchor="middle">Milo Dagwell</text>
    <rect class="frame-line" x="7.5" y="6.5" width="618" height="432"/>
  </svg>

  <svg class="poster poster--third" viewBox="0 0 633 445" xmlns="http://www.w3.org/2000/svg">
    <rect class="frame-outer" width="633" height="445"/>
    <rect class="paper" x="9" y="8" width="615" height="429"/>
    <g class="paper-hatch">
      <line x1="9" y1="40" x2="80" y2="8"/><line x1="9" y1="55" x2="110" y2="8"/><line x1="9" y1="70" x2="140" y2="8"/>
    </g>
    <g class="portrait-slot" role="img" aria-label="Black and white portrait photograph of Oswin Tarrant">
      <rect x="230" y="8" width="394" height="429" fill="url(#portraitBase)"/>
      <rect x="350" y="30" width="200" height="290" fill="url(#portraitGlow)"/>
      <rect x="340" y="260" width="300" height="200" fill="url(#portraitShade)"/>
    </g>
    <polygon class="corner-wedge" points="9,280 335,437 9,437"/>
    <line class="wedge-stripe" x1="9" y1="289" x2="316" y2="437"/>
    <line class="wedge-stripe" x1="9" y1="296" x2="302" y2="437"/>
    <line class="wedge-stripe" x1="9" y1="303" x2="288" y2="437"/>
    <polygon points="296,437 624,437 624,298" fill="url(#blueBand)"/>
    <text class="quote-text" x="64" y="91">Ever tried. Ever failed.</text>
    <text class="quote-text" x="64" y="134">No matter. Try Again.</text>
    <text class="quote-text" x="64" y="177">Fail again. Fail better.</text>
    <path class="author-pill" d="M184,242 H302 C308,236 306,228 300,221 C320,226 333,240 331,258 A15,15 0 0 1 316,274 H184 A16,16 0 0 1 184,242 Z"/>
    <text class="author-name" x="250" y="264" text-anchor="middle">Oswin Tarrant</text>
    <rect class="frame-line" x="7.5" y="6.5" width="618" height="432"/>
  </svg>

</main>
</body>
</html>
```